Business Card Design

IT Solutions company.

I need a professional looking design with my company logo if possible.

Logo is located here:
http://www.brivelsystems.co.uk/dev/images/logo1.jpg
Feel free to redesign the logo if you think you have any better suggestions.

Our services include, IT Infrastructure/Telephony Maintenance & Hosting Services. Linux and Windows Solutions, App Development.

Out website is currently under development:
http://www.brivelsystems.co.uk/dev/

I'm looking for a colourful but professional looking business card.

Industry/Entity Type

Business

Contact Information for Business Card

Brivel Systems Group Ltd
Morven Halsey
07845193870
www.brivelsystems.co.uk
mhalsey@brivelsystems.co.uk

```html
<!DOCTYPE html>
<html lang="en">
<head>
<meta charset="utf-8">
<title>Brivel Systems Group Ltd — Business Card</title>
<link rel="stylesheet" href="https://fonts.googleapis.com/css2?family=Open+Sans:wght@400;600&display=swap">
<style>
  :root {
    --backdrop: #2b2b2d;
    --paper: #ffffff;
    --navy: #1b1766;
    --navy-deep: #28235f;
    --periwinkle: #8796cc;
    --brand-blue: #1f3c9c;
    --ink: #111111;
    --soft-icon: #3a3580;
    --divider: #4a46a0;
  }
  * { box-sizing: border-box; margin: 0; padding: 0; }
  html, body { width: 1200px; height: 1000px; overflow: hidden; }
  body {
    background: var(--backdrop);
    font-family: "Open Sans", Arial, sans-serif;
    position: relative;
  }
  .card {
    position: absolute;
    left: 250px;
    width: 700px;
    height: 400px;
    overflow: hidden;
    box-shadow: 0 10px 30px rgba(0,0,0,.45);
  }
  .card--front { top: 70px; }
  .card--back { top: 530px; }

  /* front */
  .front-brand {
    height: 120px;
    background: var(--paper);
    display: flex;
    align-items: center;
    padding-left: 48px;
    gap: 14px;
  }
  .brand-dot {
    width: 34px; height: 34px;
    border-radius: 50%;
    background: var(--brand-blue);
  }
  .brand-name {
    font-weight: 600;
    font-size: 26px;
    color: var(--brand-blue);
  }
  .front-contact {
    height: 140px;
    background: var(--navy);
    display: flex;
  }
  .contact-phone {
    width: 240px;
    border-right: 1px solid var(--divider);
    display: flex;
    flex-direction: column;
    align-items: center;
    justify-content: center;
    gap: 10px;
  }
  .contact-online {
    flex: 1;
    display: flex;
    flex-direction: column;
    justify-content: center;
    gap: 16px;
    padding-left: 44px;
  }
  .contact-line {
    display: flex;
    align-items: center;
    gap: 18px;
  }
  .contact-text {
    color: var(--paper);
    font-size: 15px;
  }
  .front-person {
    height: 140px;
    background: var(--periwinkle);
    display: flex;
    flex-direction: column;
    justify-content: center;
    padding-left: 330px;
  }
  .person-name {
    font-weight: 600;
    font-size: 30px;
    color: var(--ink);
    border-bottom: 2px solid var(--ink);
    align-self: flex-start;
    line-height: 1.2;
  }
  .person-role {
    font-size: 17px;
    color: var(--ink);
    margin-top: 4px;
  }

  /* back */
  .card--back {
    background: var(--navy-deep);
    display: flex;
    align-items: center;
  }
  .back-band {
    width: 100%;
    height: 150px;
    background: var(--paper);
    display: flex;
    align-items: center;
    justify-content: center;
    gap: 16px;
  }
  .back-band .brand-name { font-size: 32px; }
  .back-band .brand-dot { width: 42px; height: 42px; }
</style>
</head>
<body>
  <section class="card card--front" aria-label="Business card front">
    <div class="front-brand">
      <span class="brand-dot"></span>
      <span class="brand-name">Brivel Systems Group Ltd</span>
    </div>
    <div class="front-contact">
      <div class="contact-phone">
        <svg class="icon-phone" width="56" height="56" viewBox="0 0 56 56" aria-hidden="true">
          <circle cx="28" cy="28" r="28" fill="var(--soft-icon)"/>
          <rect x="15" y="17" width="26" height="24" rx="4" fill="var(--navy)"/>
          <rect x="13" y="13" width="30" height="7" rx="3" fill="var(--navy)"/>
          <g fill="var(--soft-icon)">
            <rect x="20" y="24" width="4" height="3"/><rect x="26" y="24" width="4" height="3"/><rect x="32" y="24" width="4" height="3"/>
            <rect x="20" y="29" width="4" height="3"/><rect x="26" y="29" width="4" height="3"/><rect x="32" y="29" width="4" height="3"/>
            <rect x="20" y="34" width="4" height="3"/><rect x="26" y="34" width="4" height="3"/><rect x="32" y="34" width="4" height="3"/>
          </g>
        </svg>
        <span class="contact-text">07845193870</span>
      </div>
      <div class="contact-online">
        <div class="contact-line">
          <svg width="36" height="36" viewBox="0 0 36 36" aria-hidden="true">
            <circle cx="18" cy="18" r="18" fill="var(--soft-icon)"/>
            <rect x="9" y="12" width="18" height="12" fill="none" stroke="var(--navy)" stroke-width="2"/>
            <path d="M9 12 L18 19 L27 12" fill="none" stroke="var(--navy)" stroke-width="2"/>
          </svg>
          <span class="contact-text">mhalsey@brivelsystems.co.uk</span>
        </div>
        <div class="contact-line">
          <svg width="36" height="36" viewBox="0 0 36 36" aria-hidden="true">
            <circle cx="18" cy="18" r="18" fill="var(--soft-icon)"/>
            <g fill="none" stroke="var(--navy)" stroke-width="1.8">
              <circle cx="18" cy="18" r="10"/>
              <ellipse cx="18" cy="18" rx="4.5" ry="10"/>
              <line x1="8" y1="18" x2="28" y2="18"/>
              <line x1="10" y1="13" x2="26" y2="13"/>
              <line x1="10" y1="23" x2="26" y2="23"/>
            </g>
          </svg>
          <span class="contact-text">www.brivelsystems.co.uk</span>
        </div>
      </div>
    </div>
    <div class="front-person">
      <span class="person-name">Morven Halsey</span>
      <span class="person-role">Director</span>
    </div>
  </section>

  <section class="card card--back" aria-label="Business card back">
    <div class="back-band">
      <span class="brand-dot"></span>
      <span class="brand-name">Brivel Systems Group Ltd</span>
    </div>
  </section>
</body>
</html>
```